Coffeeshop menu for filter tip

We want to have a cannabis (coffeeshop) menu in the size 25mm wide x 60mm wide. Some examples attached.

it must have the following text:
Menu

WEED p/g
Velotrine €16
Cinderfox €14
Tide Rambler €14
Marigolden €16
Grand Pelican €14
Copper Comet €14

HASH p/g
Baltic Ember €12
Harbor Velvet€11
Plum Rova €14
Dusk Maple €10

Target Market(s)

tourist in Amsterdam

Requirements
Nice to have
• cannabis sign leaf
• No Cigarettes allowed symbol

```html
<!DOCTYPE html>
<html lang="en">
<head>
<meta charset="utf-8">
<title>Coffeeshop Menu – Filter Tip Samples</title>
<link rel="stylesheet" href="https://fonts.googleapis.com/css2?family=Anton&family=Roboto+Condensed:wght@400&family=Roboto+Slab:wght@300;400;700;800&display=swap">
<style>
  :root {
    --stage: #d9d9d9;
    --stage-light: #ececec;
    --label: #444;
    --red: #d10a0a;
    --red-deep: #8e0000;
    --yellow: #f2c500;
    --ink-light: #f4f4f4;
    --ink-dark: #3e3e3e;
    --skyline: #575757;
    --band-red: #c0080b;
  }
  * { margin: 0; padding: 0; box-sizing: border-box; }
  html, body { width: 1200px; height: 985px; overflow: hidden; }
  body {
    background: radial-gradient(ellipse at 50% 40%, var(--stage-light) 0%, var(--stage) 100%);
    position: relative;
    font-family: "Roboto Condensed", sans-serif;
  }
  .sample-label {
    position: absolute; top: 54px;
    font-family: "Roboto Slab", serif; font-weight: 300;
    font-size: 17px; letter-spacing: 1.5px; color: var(--label);
  }
  .menu-card {
    position: absolute; top: 92px; width: 316px; height: 836px;
    overflow: hidden;
    box-shadow: 0 14px 18px -10px rgba(0,0,0,0.45);
  }
  .menu-card--black { left: 69px; background: linear-gradient(180deg, #141414 0%, #1d1e21 60%, #202228 100%); }
  .menu-card--wine  { left: 445px; background: linear-gradient(180deg, #1a0000 0%, #4a0204 40%, #3a0410 65%, #0e1433 100%); }
  .menu-card--white { left: 819px; background: linear-gradient(180deg, #ffffff 0%, #f1f1f1 100%); }

  .leaf-decor {
    position: absolute; inset: 0;
    background:
      radial-gradient(circle at 20% 15%, rgba(255,255,255,0.05) 0, transparent 40%),
      radial-gradient(circle at 85% 85%, rgba(255,255,255,0.06) 0, transparent 35%);
  }
  .menu-card--white .leaf-decor {
    background:
      radial-gradient(circle at 90% 30%, rgba(0,0,0,0.05) 0, transparent 30%),
      radial-gradient(circle at 85% 85%, rgba(0,0,0,0.06) 0, transparent 35%);
  }

  .skyline {
    position: absolute; left: 75px; top: 42px; width: 181px; height: 66px;
    background: linear-gradient(180deg, rgba(87,87,87,0) 0%, rgba(87,87,87,0.55) 45%, var(--skyline) 100%);
  }
  .menu-card--white .skyline {
    background: linear-gradient(180deg, rgba(58,58,58,0) 0%, rgba(58,58,58,0.6) 45%, #3a3a3a 100%);
  }

  .city {
    position: absolute; top: 110px; left: 0; right: 0; text-align: center;
    font-family: "Roboto Slab", serif; font-weight: 400;
    font-size: 27px; line-height: 32px; letter-spacing: 1.5px; color: #fff;
  }
  .menu-card--white .city { color: var(--band-red); }

  .title {
    position: absolute; top: 149px; left: 0; right: 0; text-align: center;
    font-family: "Anton", sans-serif; font-weight: 400;
    font-size: 84px; line-height: 84px;
    transform: scaleX(1.08);
    color: var(--red);
    background: linear-gradient(180deg, #ff2a1a 0%, var(--red) 55%, var(--red-deep) 100%);
    -webkit-background-clip: text; background-clip: text;
    -webkit-text-fill-color: transparent;
  }

  .section-head {
    position: absolute; left: 0; right: 0; height: 40px;
    display: flex; justify-content: space-between; align-items: center;
    padding: 0 34px 0 38px;
    font-family: "Roboto Slab", serif; font-weight: 800; font-size: 29px;
    color: var(--yellow);
    text-shadow: 1px 1px 0 var(--red), -1px 0 0 var(--red), 0 -1px 0 var(--red);
  }
  .section-head--weed { top: 268px; }
  .section-head--hash { top: 549px; }
  .menu-card--white .section-head {
    background: var(--band-red); color: #fff; text-shadow: none; letter-spacing: 1px;
  }
  .menu-card--white .section-head--weed { top: 266px; }
  .menu-card--white .section-head--hash { top: 548px; }

  .price-list { position: absolute; left: 40px; width: 240px; list-style: none; }
  .price-list--weed { top: 313px; }
  .price-list--hash { top: 598px; }
  .price-list li {
    display: flex; height: 34px; line-height: 34px;
    font-size: 24px; color: var(--ink-light);
  }
  .price-list .strain { flex: 1; }
  .price-list .price { width: 44px; }
  .menu-card--white .price-list li { color: var(--ink-dark); }

  .divider {
    position: absolute; top: 533px; left: 75px; width: 168px; height: 2px;
    background: linear-gradient(90deg, transparent, var(--red-deep) 30%, var(--red-deep) 70%, transparent);
  }

  .no-smoking {
    position: absolute; top: 768px; left: 59px; right: 0; height: 26px;
    background: var(--yellow);
    font-family: "Roboto Slab", serif; font-weight: 700; font-size: 21px;
    letter-spacing: 2px; line-height: 26px; color: #111;
    padding-left: 35px;
  }
  .no-smoking-icon { position: absolute; top: 757px; left: 37px; width: 44px; height: 44px; }
</style>
</head>
<body>

<span class="sample-label" style="left:69px">SAMPLE 1</span>
<span class="sample-label" style="left:442px">SAMPLE 2</span>
<span class="sample-label" style="left:819px">SAMPLE 3</span>

<section class="menu-card menu-card--black">
  <div class="leaf-decor" role="img" aria-label="Faint cannabis leaf illustrations in the background"></div>
  <div class="skyline" role="img" aria-label="Amsterdam canal house skyline silhouette with windmill"></div>
  <p class="city">AMSTERDAM</p>
  <h1 class="title">MENU</h1>
  <h2 class="section-head section-head--weed"><span>WEED</span><span>p/g</span></h2>
  <ul class="price-list price-list--weed">
    <li><span class="strain">Velotrine</span><span class="price">€16</span></li>
    <li><span class="strain">Cinderfox</span><span class="price">€14</span></li>
    <li><span class="strain">Tide Rambler</span><span class="price">€14</span></li>
    <li><span class="strain">Marigolden</span><span class="price">€16</span></li>
    <li><span class="strain">Grand Pelican</span><span class="price">€14</span></li>
    <li><span class="strain">Copper Comet</span><span class="price">€14</span></li>
  </ul>
  <div class="divider"></div>
  <h2 class="section-head section-head--hash"><span>HASH</span><span>p/g</span></h2>
  <ul class="price-list price-list--hash">
    <li><span class="strain">Baltic Ember</span><span class="price">€12</span></li>
    <li><span class="strain">Harbor Velvet</span><span class="price">€11</span></li>
    <li><span class="strain">Plum Rova</span><span class="price">€14</span></li>
    <li><span class="strain">Dusk Maple</span><span class="price">€10</span></li>
  </ul>
  <p class="no-smoking">NO SMOKING</p>
  <svg class="no-smoking-icon" viewBox="0 0 44 44" aria-hidden="true">
    <circle cx="22" cy="22" r="19" fill="#fff" stroke="#d10a0a" stroke-width="4"/>
    <rect x="9" y="21" width="22" height="5" fill="#222"/>
    <rect x="31" y="21" width="4" height="5" fill="#222"/>
    <path d="M30 18 q-3 -4 1 -8" fill="none" stroke="#222" stroke-width="2"/>
    <line x1="9" y1="9" x2="35" y2="35" stroke="#d10a0a" stroke-width="4"/>
  </svg>
</section>

<section class="menu-card menu-card--wine">
  <div class="leaf-decor" role="img" aria-label="Faint cannabis leaf illustrations in the background"></div>
  <div class="skyline" role="img" aria-label="Amsterdam canal house skyline silhouette with windmill"></div>
  <p class="city">AMSTERDAM</p>
  <h1 class="title">MENU</h1>
  <h2 class="section-head section-head--weed"><span>WEED</span><span>p/g</span></h2>
  <ul class="price-list price-list--weed">
    <li><span class="strain">Velotrine</span><span class="price">€16</span></li>
    <li><span class="strain">Cinderfox</span><span class="price">€14</span></li>
    <li><span class="strain">Tide Rambler</span><span class="price">€14</span></li>
    <li><span class="strain">Marigolden</span><span class="price">€16</span></li>
    <li><span class="strain">Grand Pelican</span><span class="price">€14</span></li>
    <li><span class="strain">Copper Comet</span><span class="price">€14</span></li>
  </ul>
  <div class="divider"></div>
  <h2 class="section-head section-head--hash"><span>HASH</span><span>p/g</span></h2>
  <ul class="price-list price-list--hash">
    <li><span class="strain">Baltic Ember</span><span class="price">€12</span></li>
    <li><span class="strain">Harbor Velvet</span><span class="price">€11</span></li>
    <li><span class="strain">Plum Rova</span><span class="price">€14</span></li>
    <li><span class="strain">Dusk Maple</span><span class="price">€10</span></li>
  </ul>
  <p class="no-smoking">NO SMOKING</p>
  <svg class="no-smoking-icon" viewBox="0 0 44 44" aria-hidden="true">
    <circle cx="22" cy="22" r="19" fill="#fff" stroke="#d10a0a" stroke-width="4"/>
    <rect x="9" y="21" width="22" height="5" fill="#222"/>
    <rect x="31" y="21" width="4" height="5" fill="#222"/>
    <path d="M30 18 q-3 -4 1 -8" fill="none" stroke="#222" stroke-width="2"/>
    <line x1="9" y1="9" x2="35" y2="35" stroke="#d10a0a" stroke-width="4"/>
  </svg>
</section>

<section class="menu-card menu-card--white">
  <div class="leaf-decor" role="img" aria-label="Faint cannabis leaf line drawings in the background"></div>
  <div class="skyline" role="img" aria-label="Amsterdam canal house skyline silhouette with windmill"></div>
  <p class="city">AMSTERDAM</p>
  <h1 class="title">MENU</h1>
  <h2 class="section-head section-head--weed"><span>WEED</span><span>p/g</span></h2>
  <ul class="price-list price-list--weed">
    <li><span class="strain">Velotrine</span><span class="price">€16</span></li>
    <li><span class="strain">Cinderfox</span><span class="price">€14</span></li>
    <li><span class="strain">Tide Rambler</span><span class="price">€14</span></li>
    <li><span class="strain">Marigolden</span><span class="price">€16</span></li>
    <li><span class="strain">Grand Pelican</span><span class="price">€14</span></li>
    <li><span class="strain">Copper Comet</span><span class="price">€14</span></li>
  </ul>
  <h2 class="section-head section-head--hash"><span>HASH</span><span>p/g</span></h2>
  <ul class="price-list price-list--hash">
    <li><span class="strain">Baltic Ember</span><span class="price">€12</span></li>
    <li><span class="strain">Harbor Velvet</span><span class="price">€11</span></li>
    <li><span class="strain">Plum Rova</span><span class="price">€14</span></li>
    <li><span class="strain">Dusk Maple</span><span class="price">€10</span></li>
  </ul>
  <p class="no-smoking">NO SMOKING</p>
  <svg class="no-smoking-icon" viewBox="0 0 44 44" aria-hidden="true">
    <circle cx="22" cy="22" r="19" fill="#fff" stroke="#d10a0a" stroke-width="4"/>
    <rect x="9" y="21" width="22" height="5" fill="#222"/>
    <rect x="31" y="21" width="4" height="5" fill="#222"/>
    <path d="M30 18 q-3 -4 1 -8" fill="none" stroke="#222" stroke-width="2"/>
    <line x1="9" y1="9" x2="35" y2="35" stroke="#d10a0a" stroke-width="4"/>
  </svg>
</section>

</body>
</html>
```